Executive Coach needs elegant business card design

I need a business card design which includes following info: name, email (same as name, @gmail.com), phone. I'd put that on one side. On the other side i'd like some graphic indicating what i do:
- using questions to help people get great results
- encourage people to try different solutions to overcome old problems
- untangling the mental knot that traps people in vicious circles
- question mental models to get people to see a different point of view.

I'd like an elegant design. Bonus points for providing a different twist on things. I've included 2 designs I started with. Feel free to improve or discard them :-)

```html
<!DOCTYPE html>
<html lang="en">
<head>
<meta charset="utf-8">
<title>Laurent Verbeke – Executive Coach business cards</title>
<link rel="stylesheet" href="https://fonts.googleapis.com/css2?family=Quicksand:wght@400;500;700&display=swap">
<style>
  :root {
    --backdrop: #e9e7e3;
    --card-light: #f7f7f7;
    --card-mid: #d9d9d9;
    --card-dark: #bdbdbd;
    --band-blue: #29b6e0;
    --band-blue-deep: #1aa3d1;
    --band-blue-soft: #6fd0ee;
    --icon-circle: #a9d3e8;
    --ink: #1d1d1d;
    --ink-soft: #3a3a3a;
  }
  * { box-sizing: border-box; margin: 0; padding: 0; }
  html, body {
    width: 1200px; height: 723px; overflow: hidden;
    background: var(--backdrop);
    font-family: "Quicksand", "Trebuchet MS", sans-serif;
    color: var(--ink);
  }
  .stage {
    width: 1200px; height: 723px;
    display: flex; justify-content: center; align-items: center; gap: 80px;
  }
  .card {
    position: relative;
    width: 370px; height: 620px;
    background: linear-gradient(125deg, var(--card-light) 0%, var(--card-mid) 45%, var(--card-light) 62%, var(--card-dark) 100%);
    box-shadow: 0 10px 28px rgba(0,0,0,.18);
    overflow: hidden;
  }

  /* brand: plain circle with the wordmark */
  .brand {
    position: absolute; left: 0; right: 0;
    display: flex; justify-content: center; align-items: center; gap: 10px;
    font-size: 22px; font-weight: 700; color: var(--ink);
    letter-spacing: .5px;
  }
  .brand__dot {
    width: 22px; height: 22px; border-radius: 50%;
    background: var(--ink);
  }
  .card--front .brand { top: 110px; }
  .card--back .brand { top: 230px; }

  /* front: contact side */
  .title-line {
    position: absolute; top: 196px; left: 96px;
    display: inline-block; white-space: nowrap;
    padding: 6px 22px 6px 22px;
    background: linear-gradient(90deg, var(--band-blue-soft), var(--band-blue));
    font-size: 24px; font-weight: 500;
  }
  .title-line strong { font-weight: 700; }
  .name-line {
    position: absolute; top: 250px; left: 40px;
    display: flex; align-items: center; white-space: nowrap;
    font-size: 30px;
  }
  .name-line__first {
    display: inline-block;
    padding: 5px 8px 5px 16px;
    background: linear-gradient(90deg, var(--band-blue), var(--band-blue-deep));
    font-weight: 400;
  }
  .name-line__last { font-weight: 700; padding-left: 2px; }

  .contact {
    position: absolute; left: 0; right: 0;
    display: flex; flex-direction: column; align-items: center;
    font-size: 18px; font-weight: 500; color: var(--ink-soft);
  }
  .contact--email { top: 340px; }
  .contact--phone { top: 430px; }
  .contact__icon {
    width: 42px; height: 42px; border-radius: 50%;
    background: var(--icon-circle);
    display: flex; align-items: center; justify-content: center;
    margin-bottom: 8px;
  }

  /* back: identity side */
  .identity-band {
    position: absolute; top: 330px; left: 0;
    width: 320px; height: 100px;
    background: linear-gradient(90deg, var(--band-blue-soft) 0%, var(--band-blue) 40%, var(--band-blue-deep) 100%);
    padding: 14px 0 0 28px;
    white-space: nowrap;
  }
  .identity-band__name { font-size: 32px; font-weight: 400; line-height: 1.1; }
  .identity-band__name strong { font-weight: 700; }
  .identity-band__role { font-size: 22px; font-weight: 500; margin-top: 6px; padding-left: 8px; }
</style>
</head>
<body>
<main class="stage">
  <section class="card card--front">
    <div class="brand"><span class="brand__dot"></span>Clearpath</div>
    <div class="title-line">Executive <strong>Coach</strong></div>
    <div class="name-line">
      <span class="name-line__first">Laurent</span><span class="name-line__last">Verbeke</span>
    </div>
    <div class="contact contact--email">
      <span class="contact__icon">
        <svg width="20" height="14" viewBox="0 0 20 14" aria-hidden="true">
          <rect x="1" y="1" width="18" height="12" fill="none" stroke="#1d1d1d" stroke-width="1.5"/>
          <path d="M1 1 L10 8 L19 1" fill="none" stroke="#1d1d1d" stroke-width="1.5"/>
        </svg>
      </span>
      laurent.verbeke@postbox.net
    </div>
    <div class="contact contact--phone">
      <span class="contact__icon">
        <svg width="14" height="22" viewBox="0 0 14 22" aria-hidden="true">
          <rect x="1" y="1" width="12" height="20" rx="2" fill="none" stroke="#1d1d1d" stroke-width="1.5"/>
          <line x1="1" y1="16" x2="13" y2="16" stroke="#1d1d1d" stroke-width="1.2"/>
          <circle cx="7" cy="18.5" r="1" fill="#1d1d1d"/>
        </svg>
      </span>
      61834527
    </div>
  </section>

  <section class="card card--back">
    <div class="brand"><span class="brand__dot"></span>Clearpath</div>
    <div class="identity-band">
      <div class="identity-band__name">Laurent<strong>Verbeke</strong></div>
      <div class="identity-band__role">Executive Coach</div>
    </div>
  </section>
</main>
</body>
</html>
```